JMT - Business Card Design Project

We need a business card based on our logo
Updates

Hi I just upload logo file in AI format Thanks and regards

Target Market(s)

Bank, Big companies, Business owners

Industry/Entity Type

Business

Font styles to use
Sans Serif

```html
<!DOCTYPE html>
<html lang="en">
<head>
<meta charset="utf-8">
<title>JMT – Business Card</title>
<link rel="stylesheet" href="https://fonts.googleapis.com/css2?family=Source+Sans+3:wght@300;400&display=swap">
<style>
  :root {
    --backdrop: #1c1c1c;
    --card: #ffffff;
    --navy: #1b2c54;
    --grey: #8c9196;
  }
  html, body {
    margin: 0;
    padding: 0;
    width: 1200px;
    height: 927px;
    overflow: hidden;
    background: var(--backdrop);
  }
  .stage {
    position: relative;
    width: 1200px;
    height: 927px;
  }
  .business-card {
    position: absolute;
    left: 277px;
    top: 257px;
    width: 634px;
    height: 362px;
    background: var(--card);
    font-family: "Source Sans 3", "Helvetica Neue", Arial, sans-serif;
  }
  .brand-name {
    position: absolute;
    left: 57px;
    top: 104px;
    margin: 0;
    font-size: 110px;
    font-weight: 400;
    line-height: 1;
    letter-spacing: -2px;
    color: var(--navy);
  }
  .holder {
    position: absolute;
    left: 366px;
    top: 46px;
  }
  .holder-name {
    margin: 0;
    font-size: 34px;
    font-weight: 300;
    line-height: 1;
    color: var(--navy);
    letter-spacing: 0.5px;
  }
  .holder-role {
    margin: 2px 0 0;
    font-size: 19px;
    font-weight: 300;
    line-height: 1.1;
    color: var(--grey);
  }
  .contact-list {
    position: absolute;
    left: 366px;
    top: 239px;
    margin: 0;
    padding: 0;
    list-style: none;
    font-size: 18.5px;
    font-weight: 300;
    line-height: 24px;
    color: var(--grey);
  }
</style>
</head>
<body>
  <main class="stage">
    <article class="business-card">
      <p class="brand-name">JMT</p>
      <header class="holder">
        <h1 class="holder-name">DANIEL OKORO</h1>
        <p class="holder-role">DIRECTOR</p>
      </header>
      <ul class="contact-list">
        <li class="contact-phone">+65 9000 4417</li>
        <li class="contact-email">info@jmtconseil.com</li>
        <li class="contact-web">www.jmtconseil.com</li>
      </ul>
    </article>
  </main>
</body>
</html>
```